Business Card Design and Logo Needed

I need Business Cards and a Logo for my website and public speaking business which can be found at: www.kelsa-thorn.example

I'm looking for creative and unique ideas. Some business cards I've found online that I like can be found at:
http://gigplatelo.example/general/18-smokin-hot-business-card-designs/

and at

http://www.vortaplume.example/2009/04/50-creative-business-cards-of-50-graphic-designers/

```html
<!DOCTYPE html>
<html lang="en">
<head>
<meta charset="utf-8">
<title>Kelsa Thorn — Business Card</title>
<link rel="stylesheet" href="https://fonts.googleapis.com/css2?family=Ubuntu:wght@300;400;700&display=swap">
<style>
  :root {
    --backdrop: #d6a77c;
    --leaf: #82ad00;
    --paper: #ffffff;
    --ink-on-leaf: #ffffff;
    --mark-faint: rgba(255, 255, 255, 0.28);
  }
  * { box-sizing: border-box; margin: 0; padding: 0; }
  html, body { width: 1200px; height: 849px; overflow: hidden; }
  body {
    position: relative;
    background: var(--backdrop);
    font-family: "Ubuntu", sans-serif;
  }
  .card {
    position: absolute;
    top: 304px;
    width: 528px;
    height: 265px;
    overflow: hidden;
  }
  .card--front { left: 60px; background: var(--leaf); }
  .card--back { left: 611px; background: var(--leaf); }

  .front__panel {
    position: absolute;
    left: 0; top: 0;
    width: 165px; height: 100%;
    background: var(--paper);
  }
  .brand-tag {
    position: absolute;
    left: 18px; top: 34px;
    display: flex;
    align-items: center;
    gap: 7px;
    color: var(--leaf);
    font-size: 13px;
    font-weight: 400;
  }
  .brand-tag__dot {
    width: 12px; height: 12px;
    border-radius: 50%;
    background: var(--leaf);
  }
  .identity {
    position: absolute;
    left: 88px; top: 84px;
    height: 150px;
    writing-mode: vertical-rl;
    transform: rotate(180deg);
    color: var(--leaf);
  }
  .identity__name {
    font-size: 22px;
    font-weight: 300;
    line-height: 30px;
    letter-spacing: 0.3px;
  }
  .identity__role {
    font-size: 6.5px;
    font-weight: 400;
    line-height: 12px;
  }

  .contact {
    position: absolute;
    left: 199px; top: 86px;
    color: var(--ink-on-leaf);
    font-size: 14px;
    line-height: 19px;
  }
  .contact p { margin-bottom: 18px; }
  .contact strong { font-weight: 700; }
  .contact__web { font-weight: 700; }

  .back__mark {
    position: absolute;
    left: 50%; top: 50%;
    transform: translate(-50%, -50%);
    display: flex;
    align-items: center;
    gap: 12px;
    color: var(--mark-faint);
    font-size: 30px;
    font-weight: 400;
    white-space: nowrap;
  }
  .back__dot {
    width: 22px; height: 22px;
    border-radius: 50%;
    background: var(--mark-faint);
  }
</style>
</head>
<body>
  <section class="card card--front" aria-label="Business card front">
    <div class="front__panel">
      <div class="brand-tag"><span class="brand-tag__dot"></span><span>Kelsa Thorn</span></div>
      <div class="identity">
        <div class="identity__name">Kelsa Thorn</div>
        <div class="identity__role">Public Speaker &amp; Philanthropist</div>
      </div>
    </div>
    <div class="contact">
      <p>2190 Meridale Avenue, Suite 400<br>Houston, Texas 77099</p>
      <p><strong>Phone</strong> 713 555 0148<br>
         <strong>Fax</strong> 713 555 0192<br>
         <strong>Email</strong> info@kelsathorn.example</p>
      <p class="contact__web">www.kelsa-thorn.example</p>
    </div>
  </section>

  <section class="card card--back" aria-label="Business card back">
    <div class="back__mark"><span class="back__dot"></span><span>Kelsa Thorn</span></div>
  </section>
</body>
</html>
```